Business Card/Design Project for Personal Injury Lawyer

Personal Injury Attorney. I represent people who have been injured in accidents and are making money damage claims against the negligent party. As a personal injury attorney, I am a counselor, advisor, and legal representative to my clients. Clients want someone who is aggresssive yet professional.

More information about what I do an be found at www.vorlandlaw.example

Target Market(s)

General public.

Industry/Entity Type

Legal

Contact Information for Business Card

Need a new logo/brand image for b-cards, website, and letterhead/envelops. Looking for something original (no scales of justice or courthouse columns), yet classy and professional.

Here's what I'm thinking (but I'm always open to other ideas):

On the front, I would like my name (Colton R. Vorland), and underneath the words "Personal Injury Attorney." The background could be black, for example, and the lettering could be white or foil. I'm open to differnt colors, or even two colors. My name on the front side should pop.

And then on the back would be all my contact info, and maybe a logo or a slogan.

Here are two slogans I've come up with so far: 1. Right By You. 2. Serious Results for the Seriously Injured.

Requirements
Must have
• Something that identifys me as a personal injury attorney, such as the words Personal Injury Attorney (or Lawyer, or Law Firm, etc.).
Nice to have
• A style/image that can be used nicely on my website and on letterhead.
Should not have
• Tired, commonly used logos or symbols, such a scales of justice or courthouse columns.

```html
<!DOCTYPE html>
<html lang="en">
<head>
<meta charset="utf-8">
<title>Colton R. Vorland – Business Card</title>
<link rel="stylesheet" href="https://fonts.googleapis.com/css2?family=Cinzel:wght@400;500&family=Open+Sans:wght@400&display=swap">
<style>
  :root {
    --backdrop: #d8d8d8;
    --paper: #f4f4f2;
    --ink: #1e1e1e;
    --ink-soft: #333333;
    --card-dark: #1f1c1d;
    --card-dark-top: #3a3738;
    --gold: #a97b3f;
    --white: #f2f2f2;
    --muted: #858383;
  }
  * { box-sizing: border-box; margin: 0; padding: 0; }
  html, body { width: 1200px; height: 895px; overflow: hidden; }
  body {
    background: var(--backdrop);
    display: flex;
    align-items: center;
    justify-content: center;
    gap: 60px;
  }
  .card {
    width: 520px;
    height: 297px;
    position: relative;
    box-shadow: 0 12px 28px rgba(0,0,0,0.18);
  }

  /* Shared brand mark: square + name */
  .brand {
    display: flex;
    align-items: center;
    gap: 8px;
  }
  .brand__square {
    width: 10px;
    height: 10px;
    background: var(--gold);
    flex: none;
  }
  .brand__name {
    font-family: "Cinzel", serif;
    font-size: 13px;
    letter-spacing: 2px;
    color: var(--gold);
    white-space: nowrap;
  }

  /* Back side: contact details */
  .card--back {
    background: var(--paper);
    color: var(--ink);
    display: flex;
    align-items: center;
    justify-content: center;
  }
  .back-layout {
    display: flex;
    flex-direction: column;
    align-items: flex-start;
  }
  .back-layout .brand {
    margin-left: 96px;
    margin-bottom: 6px;
  }
  .tagline {
    font-family: "Cinzel", serif;
    font-size: 10px;
    letter-spacing: 2.5px;
    color: var(--gold);
    margin-left: 96px;
    margin-bottom: 14px;
    white-space: nowrap;
  }
  .back-name {
    font-family: "Cinzel", serif;
    font-size: 20px;
    font-weight: 500;
    letter-spacing: 1px;
    margin-bottom: 10px;
    white-space: nowrap;
  }
  .contact {
    font-family: "Open Sans", sans-serif;
    font-size: 11px;
    line-height: 1.45;
    color: var(--ink-soft);
    font-style: normal;
  }

  /* Front side: name */
  .card--front {
    background: linear-gradient(160deg, var(--card-dark-top), var(--card-dark) 55%);
    display: flex;
    flex-direction: column;
    align-items: center;
    justify-content: center;
  }
  .card--front .brand {
    margin-bottom: 18px;
  }
  .front-name {
    font-family: "Cinzel", serif;
    font-size: 24px;
    font-weight: 500;
    letter-spacing: 6px;
    color: var(--white);
    margin-bottom: 8px;
    white-space: nowrap;
  }
  .front-title {
    font-family: "Cinzel", serif;
    font-size: 12px;
    letter-spacing: 4px;
    color: var(--muted);
    white-space: nowrap;
  }
</style>
</head>
<body>
  <section class="card card--back" aria-label="Card back">
    <div class="back-layout">
      <div class="brand">
        <span class="brand__square"></span>
        <span class="brand__name">VORLAND LAW</span>
      </div>
      <p class="tagline">RIGHT BY YOU</p>
      <h2 class="back-name">Colton R. Vorland</h2>
      <address class="contact">
        420 Harbor Row - Suite 310<br>
        Bayport, Florida 33000<br>
        Phone: 555.014.2200<br>
        Fax: 555.014.2201<br>
        www.vorlandlaw.example
      </address>
    </div>
  </section>

  <section class="card card--front" aria-label="Card front">
    <div class="brand">
      <span class="brand__square"></span>
      <span class="brand__name">VORLAND LAW</span>
    </div>
    <h1 class="front-name">COLTON R. VORLAND</h1>
    <p class="front-title">PERSONAL INJURY ATTORNEY</p>
  </section>
</body>
</html>
```